Brightvale Energy International Website

Brightvale Energy – Lighting the Path of
UK Homes Sustainably.

New Launch Website

Focus on 4 Product Categories

- Solar PV
- Battery Energy Storage
- EV Charging
- Heat Pumps

Add

Energy News
Enquire Now button Top right every page
Contact us page

Follow Lumenhaus.co.uk for similar content pages

Target Market(s)

Residential home owners UK NOT US

Industry/Entity Type

Solar energy, home energy , EV charging

Coding

Coded - Design and coding required

Number of Pages Required

5+ page

Font styles to use
Sans Serif

Colors
0054AA
0677BA
7BADD7
CADEEF
E8F1F8
59FF00
82FF00
B8FF75
E3FFCB
F4FFEA
FFF300
FFF600
FEFA6F
FFFEC7
FFFEE8

Requirements
Must have
• Strong brand logo on every page, clear content bar
Nice to have
• Add these logos from LumenHaus.co.uk

```html
<!DOCTYPE html>
<html lang="en">
<head>
<meta charset="utf-8">
<title>Brightvale Energy – Lighting the Path of UK Homes</title>
<link href="https://fonts.googleapis.com/css2?family=Poppins:wght@400;500;600;700&display=swap" rel="stylesheet">
<style>
:root{
  --navy:#0c2c62;
  --navy-deep:#08214b;
  --green:#2e9e3e;
  --green-bright:#3cb043;
  --green-dark:#1f7a2e;
  --ink:#111a2b;
  --muted:#4a5366;
  --white:#ffffff;
}
*{box-sizing:border-box;margin:0;padding:0}
html,body{width:1200px;height:4800px;overflow:hidden}
body{font-family:'Poppins',sans-serif;color:var(--ink);background:var(--white);position:relative}
section,header,footer{position:absolute;left:0;width:1200px}
.abs{position:absolute}

/* nav */
.site-header{top:0;height:112px;background:var(--white);display:flex;align-items:center;padding:0 56px;box-shadow:0 2px 10px rgba(0,0,0,.06);z-index:2;white-space:nowrap}
.brand{font-weight:700;font-size:28px;color:var(--ink);letter-spacing:-.3px;white-space:nowrap}
.nav{display:flex;gap:30px;margin-left:auto;margin-right:32px;font-size:15px;font-weight:500;color:var(--ink)}
.nav a{color:inherit;text-decoration:none;position:relative;white-space:nowrap}
.nav a.active{color:var(--green)}
.nav a.active::after{content:"";position:absolute;left:0;right:0;bottom:-8px;height:3px;background:var(--green)}
.btn{display:inline-flex;align-items:center;justify-content:center;gap:12px;border-radius:40px;font-weight:500;text-decoration:none;white-space:nowrap}
.btn-quote{background:var(--green);color:var(--white);font-size:15px;height:50px;padding:0 24px}

/* hero */
.hero{top:112px;height:548px;overflow:hidden}
.hero-photo{position:absolute;inset:0;background:linear-gradient(180deg,#9cb8cf 0%,#c9d6df 35%,#5f6e6c 62%,#2d3d52 80%,#1e2d45 100%)}
.hero-panel{position:absolute;inset:0;background:linear-gradient(100deg,rgba(46,158,62,.95) 0%,rgba(46,158,62,.85) 38%,rgba(46,158,62,0) 56%)}
.hero-content{position:absolute;left:112px;top:118px;width:620px;color:var(--white)}
.hero h1{font-size:56px;line-height:64px;font-weight:700}
.hero p{font-size:19px;line-height:30px;margin-top:22px}
.btn-hero{background:var(--green-dark);color:var(--white);height:56px;padding:0 28px;font-size:17px;margin-top:30px}
.arrow-dot{width:30px;height:30px;border-radius:50%;background:var(--white);display:inline-flex;align-items:center;justify-content:center}

/* shared headings */
.eyebrow{display:flex;align-items:center;justify-content:center;gap:14px;font-size:14px;font-weight:600;letter-spacing:1px;color:var(--ink)}
.eyebrow::before{content:"";width:60px;height:3px;background:var(--green)}
.section-title{text-align:center;font-size:42px;font-weight:700;margin-top:14px}
.lead{text-align:center;font-size:18px;line-height:32px;color:var(--muted)}

/* solutions */
.solutions{top:660px;height:612px;background:var(--white)}
.solutions .eyebrow{position:absolute;top:94px;width:100%}
.solutions .section-title{position:absolute;top:114px;width:100%}
.solutions .lead{position:absolute;top:182px;width:100%;font-size:17px}
.product-card{position:absolute;top:240px;width:234px;height:252px;border-radius:14px;overflow:hidden;box-shadow:0 6px 16px rgba(0,0,0,.15);background:var(--white)}
.product-card .ph{height:252px}
.product-card .caption{position:absolute;left:0;right:0;bottom:0;height:50px;background:var(--white);display:flex;align-items:center;gap:10px;padding-left:10px;font-size:15px;font-weight:500;white-space:nowrap}
.product-card .icon{flex:none;width:44px;height:44px;margin-top:-26px;border-radius:8px;background:var(--green);display:flex;align-items:center;justify-content:center}
.slider-arrow{position:absolute;top:340px}

/* about */
.about{top:1272px;height:848px;background:radial-gradient(circle at 50% 30%,#133a7a 0%,var(--navy) 55%,var(--navy-deep) 100%);color:var(--white)}
.about .eyebrow{position:absolute;top:80px;width:100%;color:var(--white)}
.about .section-title{position:absolute;top:104px;width:100%}
.about .lead{position:absolute;top:184px;left:120px;width:960px;color:#e4ebf6}
.about-photo{position:absolute;top:408px;width:460px;height:360px;border-radius:10px}

/* why */
.why{top:2120px;height:680px;background:var(--white)}
.why .eyebrow{position:absolute;top:104px;width:100%}
.why .section-title{position:absolute;top:128px;width:100%}
.why .lead{position:absolute;top:210px;left:150px;width:900px;color:var(--ink)}
.feature{position:absolute;top:360px;width:250px;height:240px;border-radius:14px;border:2px solid var(--ink);background:var(--white);text-align:center;padding-top:40px}
.feature .ficon{width:64px;height:64px;margin:0 auto;border-radius:10px;border:2px solid var(--ink);display:flex;align-items:center;justify-content:center}
.feature h3{font-size:20px;font-weight:600;margin-top:18px}
.feature p{font-size:16px;line-height:22px;color:var(--muted);margin:8px 24px 0}
.feature.featured{background:var(--navy);border-color:var(--navy);color:var(--white)}
.feature.featured .ficon{border-color:var(--white)}
.feature.featured p{color:#dfe7f3}

/* gallery */
.gallery{top:2800px;height:720px;background:repeating-linear-gradient(135deg,var(--green-bright) 0 60px,#37a93f 60px 120px)}
.gallery .eyebrow{position:absolute;top:84px;width:100%;color:var(--white)}
.gallery .eyebrow::before{background:var(--white)}
.gallery .section-title{position:absolute;top:106px;width:100%;color:var(--white)}
.gallery-photo{position:absolute;top:200px;height:320px;border-radius:14px}
.btn-gallery{position:absolute;top:560px;left:480px;width:240px;height:54px;background:var(--white);color:var(--ink);font-size:17px}
.gallery .slider-arrow{top:564px}

/* blog */
.blog{top:3520px;height:840px;background:var(--white)}
.blog .eyebrow{position:absolute;top:84px;width:100%}
.blog .section-title{position:absolute;top:110px;width:100%;font-size:44px}
.post{position:absolute;top:200px;width:288px;height:500px;border-radius:18px;background:var(--white);box-shadow:0 8px 22px rgba(0,0,0,.14);overflow:hidden}
.post .ph{height:220px;border-radius:18px 18px 0 0}
.post h3{font-size:18px;line-height:25px;font-weight:600;margin:22px 20px 0}
.post p{font-size:14px;line-height:20px;color:var(--muted);margin:10px 20px 0}
.post .btn{position:absolute;left:60px;bottom:30px;width:168px;height:48px;background:var(--green);color:var(--white);font-size:16px}
.post.dark{background:var(--navy);color:var(--white)}
.post.dark p{color:#dfe7f3}
.post.dark .btn{background:var(--white);color:var(--ink)}
.btn-all{position:absolute;top:760px;left:500px;width:200px;height:52px;background:var(--green);color:var(--white);font-size:16px}

/* footer */
.site-footer{top:4360px;height:440px;background:var(--navy-deep);color:var(--white);overflow:hidden}
.footer-col{position:absolute;top:140px;font-size:16px;line-height:22px}
.footer-col li{list-style:none;margin-bottom:20px}
.contact li{display:flex;align-items:center;gap:16px}
.footer-bottom{position:absolute;top:338px;left:112px;font-size:15px;color:#cfd8e8}
.socials{display:flex;gap:12px;margin-top:22px}
.socials span{width:30px;height:30px;border-radius:50%;background:var(--white);display:block}
.footer-brand{position:absolute;right:112px;top:330px;text-align:right}
.footer-brand .brand{color:var(--white);font-size:44px}
.footer-brand small{display:block;font-size:15px;color:#cfd8e8;margin-top:8px}
</style>
</head>
<body>

<header class="site-header">
  <div class="brand">Brightvale Energy</div>
  <nav class="nav">
    <a class="active" href="#">HOME</a>
    <a href="#">ABOUT</a>
    <a href="#">PRODUCTS</a>
    <a href="#">HOW IT WORKS</a>
    <a href="#">CASE STUDIES</a>
  </nav>
  <a class="btn btn-quote" href="#">Get a Free Quote</a>
</header>

<section class="hero">
  <div class="hero-photo" role="img" aria-label="Modern house with rooftop solar panels and ground-mounted solar array under a cloudy sky"></div>
  <div class="hero-panel"></div>
  <div class="hero-content">
    <h1>Powering the Future of UK Homes</h1>
    <p>Switch to solar, storage, EV charging, and heat pumps — all designed to cut your bills and carbon footprint.</p>
    <a class="btn btn-hero" href="#">Explore Our Solutions
      <span class="arrow-dot"><svg width="14" height="14" viewBox="0 0 14 14"><path d="M2 7h9M7 3l4 4-4 4" stroke="#1f7a2e" stroke-width="2" fill="none"/></svg></span>
    </a>
  </div>
</section>

<section class="solutions">
  <div class="eyebrow">PRODUCTS</div>
  <h2 class="section-title">Our Solutions</h2>
  <p class="lead">Harness clean energy with technology that lowers bills and powers the future.</p>

  <svg class="slider-arrow" style="left:52px" width="28" height="24" viewBox="0 0 28 24"><path d="M26 12H4M12 3l-9 9 9 9" stroke="#111a2b" stroke-width="3" fill="none"/></svg>
  <svg class="slider-arrow" style="left:1120px" width="28" height="24" viewBox="0 0 28 24"><path d="M2 12h22M16 3l9 9-9 9" stroke="#111a2b" stroke-width="3" fill="none"/></svg>

  <div class="product-card" style="left:105px">
    <div class="ph" role="img" aria-label="Solar PV panels on a house roof" style="background:linear-gradient(180deg,#8fb7d8,#3c5a82 55%,#23385a)"></div>
    <div class="caption"><span class="icon"><svg width="24" height="24" viewBox="0 0 24 24"><circle cx="12" cy="12" r="4" fill="#fff"/><path d="M12 2v3M12 19v3M2 12h3M19 12h3M5 5l2 2M17 17l2 2M5 19l2-2M17 7l2-2" stroke="#fff" stroke-width="2"/></svg></span>Solar PV</div>
  </div>
  <div class="product-card" style="left:357px">
    <div class="ph" role="img" aria-label="Battery energy storage containers outdoors" style="background:linear-gradient(180deg,#8fb7d8,#c9cdd0 55%,#9aa3a8)"></div>
    <div class="caption"><span class="icon"><svg width="24" height="24" viewBox="0 0 24 24"><rect x="4" y="6" width="14" height="12" rx="2" stroke="#fff" stroke-width="2" fill="none"/><rect x="18" y="10" width="3" height="4" fill="#fff"/></svg></span>Battery Energy Storage</div>
  </div>
  <div class="product-card" style="left:609px">
    <div class="ph" role="img" aria-label="White electric car charging at a home charger" style="background:linear-gradient(180deg,#d6d2c9,#eeeeec 50%,#8e8f8c)"></div>
    <div class="caption"><span class="icon"><svg width="24" height="24" viewBox="0 0 24 24"><path d="M13 3L6 14h5l-1 7 7-11h-5z" fill="#fff"/></svg></span>EV Charging</div>
  </div>
  <div class="product-card" style="left:861px">
    <div class="ph" role="img" aria-label="Air source heat pump units beside a building" style="background:linear-gradient(180deg,#b9c0c4,#e7e8e6 55%,#7c8489)"></div>
    <div class="caption"><span class="icon"><svg width="24" height="24" viewBox="0 0 24 24"><circle cx="12" cy="12" r="8" stroke="#fff" stroke-width="2" fill="none"/><path d="M12 4v16M4 12h16" stroke="#fff" stroke-width="2"/></svg></span>Heat Pumps</div>
  </div>
</section>

<section class="about">
  <div class="eyebrow">ABOUT</div>
  <h2 class="section-title">About Brightvale Energy</h2>
  <p class="lead">At Brightvale Energy, we believe every home can be a power station. From solar panels to battery storage, EV charging, and heat pumps, we provide integrated renewable energy solutions that lower bills, reduce carbon emissions, and future-proof your home. With years of expertise in the UK energy market, we're not just installers — we're energy partners who guide you from consultation to installation, with ongoing support and monitoring.</p>
  <div class="about-photo" style="left:112px;background:linear-gradient(180deg,#bfd4e6,#eef1f2 40%,#4b5360 70%,#6f8a5a)" role="img" aria-label="Contemporary family home with solar panels on the roof"></div>
  <div class="about-photo" style="left:628px;background:linear-gradient(180deg,#6f8fb0,#2f4763 50%,#5e6f7a)" role="img" aria-label="Family standing beside an electric car charging outside their solar-powered home"></div>
</section>

<section class="why">
  <div class="eyebrow">WHY CHOOSE US</div>
  <h2 class="section-title">Why Brightvale Energy</h2>
  <p class="lead">At Brightvale Energy, we go beyond panels and installations — we deliver end-to-end clean energy solutions tailored to UK homes. From solar and storage to EV charging and heat pumps, we provide everything you need to cut bills, reduce carbon, and future-proof your home.</p>

  <div class="feature featured" style="left:196px">
    <div class="ficon"><svg width="32" height="32" viewBox="0 0 32 32"><rect x="5" y="8" width="22" height="14" stroke="#fff" stroke-width="2" fill="none"/><path d="M5 15h22M12 8v14M20 8v14M16 22v5M11 27h10" stroke="#fff" stroke-width="2"/></svg></div>
    <h3>Sustainable Energy</h3>
    <p>Reduce your carbon footprint.</p>
  </div>
  <div class="feature" style="left:474px">
    <div class="ficon"><svg width="32" height="32" viewBox="0 0 32 32"><path d="M6 24l7-7 5 5 9-11" stroke="#111a2b" stroke-width="2.5" fill="none"/><path d="M21 11h6v6" stroke="#111a2b" stroke-width="2.5" fill="none"/></svg></div>
    <h3>Lower Bills</h3>
    <p>Cut rising energy costs with smart solar power.</p>
  </div>
  <div class="feature" style="left:752px">
    <div class="ficon"><svg width="32" height="32" viewBox="0 0 32 32"><path d="M18 4L8 18h7l-2 10 11-15h-7z" stroke="#111a2b" stroke-width="2" fill="none"/></svg></div>
    <h3>Future-Ready Tech</h3>
    <p>EV, heat, and smart storage integration.</p>
  </div>
</section>

<section class="gallery">
  <div class="eyebrow">GALLERY</div>
  <h2 class="section-title">See Our Work in Action</h2>
  <div class="gallery-photo" style="left:-24px;width:256px;background:linear-gradient(180deg,#7fa8cf,#2f4a73 60%,#1d2b45)" role="img" aria-label="Close view of rooftop solar panels"></div>
  <div class="gallery-photo" style="left:252px;width:308px;background:linear-gradient(180deg,#6e9fd0,#d9dcde 55%,#a7acae)" role="img" aria-label="Battery storage units beside a row of solar panels"></div>
  <div class="gallery-photo" style="left:600px;width:312px;background:linear-gradient(180deg,#b8a586,#d9cbb4 45%,#5d5a55)" role="img" aria-label="Row of electric vehicle charging stations at sunset"></div>
  <div class="gallery-photo" style="left:932px;width:300px;background:linear-gradient(180deg,#7aa7d8,#b6c9d9 50%,#2b4d82)" role="img" aria-label="Two installers reviewing plans on a solar rooftop"></div>
  <svg class="slider-arrow" style="left:80px" width="40" height="40" viewBox="0 0 40 40"><circle cx="20" cy="20" r="18" stroke="#fff" stroke-width="2" fill="none"/><path d="M23 12l-8 8 8 8" stroke="#fff" stroke-width="3" fill="none"/></svg>
  <svg class="slider-arrow" style="left:1080px" width="40" height="40" viewBox="0 0 40 40"><circle cx="20" cy="20" r="18" stroke="#fff" stroke-width="2" fill="none"/><path d="M17 12l8 8-8 8" stroke="#fff" stroke-width="3" fill="none"/></svg>
  <a class="btn btn-gallery" href="#">View Full Gallery
    <span class="arrow-dot" style="background:var(--green)"><svg width="14" height="14" viewBox="0 0 14 14"><path d="M2 7h9M7 3l4 4-4 4" stroke="#fff" stroke-width="2" fill="none"/></svg></span>
  </a>
</section>

<section class="blog">
  <div class="eyebrow">OUR BLOG</div>
  <h2 class="section-title">Stay Informed. Stay Sustainable.</h2>

  <article class="post dark" style="left:120px">
    <div class="ph" role="img" aria-label="Brick house with solar panels on the roof" style="background:linear-gradient(180deg,#7fb0e0,#b3c6d3 45%,#8a5a44 75%,#5e7a4a)"></div>
    <h3>Is Solar Worth It in the UK?</h3>
    <p>Learn how modern solar technology makes clean energy a smart investment — even with cloudy weather.</p>
    <a class="btn" href="#">Read More <span class="arrow-dot" style="background:var(--green)"><svg width="14" height="14" viewBox="0 0 14 14"><path d="M2 7h9M7 3l4 4-4 4" stroke="#fff" stroke-width="2" fill="none"/></svg></span></a>
  </article>
  <article class="post" style="left:456px">
    <div class="ph" role="img" aria-label="Technician installing a wall-mounted home battery" style="background:linear-gradient(180deg,#a9adb1,#d7d9da 45%,#3a4a63)"></div>
    <h3>The Future of Battery Energy Storage</h3>
    <p>Why home batteries are key to energy independence and lower bills.</p>
    <a class="btn" href="#">Read More <span class="arrow-dot"><svg width="14" height="14" viewBox="0 0 14 14"><path d="M2 7h9M7 3l4 4-4 4" stroke="#2e9e3e" stroke-width="2" fill="none"/></svg></span></a>
  </article>
  <article class="post" style="left:792px">
    <div class="ph" role="img" aria-label="Silver car plugged into a home EV charger" style="background:linear-gradient(180deg,#c9c6c0,#e4e2de 45%,#6c6d70)"></div>
    <h3>The Future of Battery Energy Storage</h3>
    <p>Why home batteries are key to energy independence and lower bills.</p>
    <a class="btn" href="#">Read More <span class="arrow-dot"><svg width="14" height="14" viewBox="0 0 14 14"><path d="M2 7h9M7 3l4 4-4 4" stroke="#2e9e3e" stroke-width="2" fill="none"/></svg></span></a>
  </article>

  <a class="btn btn-all" href="#">View All Articles</a>
</section>

<footer class="site-footer">
  <svg class="abs" style="left:0;top:0" width="1200" height="80" viewBox="0 0 1200 80" preserveAspectRatio="none">
    <path d="M0 0H1200V30C900 70 400 -10 0 40Z" fill="#ffffff"/>
    <path d="M0 40C400 -10 900 70 1200 30" stroke="#2e9e3e" stroke-width="4" fill="none"/>
  </svg>

  <ul class="footer-col contact" style="left:112px">
    <li><svg width="22" height="22" viewBox="0 0 22 22"><path d="M11 2a6 6 0 0 0-6 6c0 5 6 12 6 12s6-7 6-12a6 6 0 0 0-6-6z" fill="#fff"/><circle cx="11" cy="8" r="2.2" fill="#08214b"/></svg>48 Meadow Lane, Bristol, UK</li>
    <li><svg width="22" height="22" viewBox="0 0 22 22"><path d="M5 2h4l2 5-3 2a12 12 0 0 0 5 5l2-3 5 2v4a2 2 0 0 1-2 2C9 19 3 13 3 4a2 2 0 0 1 2-2z" fill="#fff"/></svg>+44 (0)117 496 0321</li>
    <li><svg width="22" height="22" viewBox="0 0 22 22"><rect x="2" y="5" width="18" height="13" rx="2" fill="#fff"/><path d="M3 6l8 6 8-6" stroke="#08214b" stroke-width="1.6" fill="none"/></svg>hello@brightvaleenergy.co.uk</li>
  </ul>
  <ul class="footer-col" style="left:576px">
    <li>Home</li><li>About</li><li>Products</li><li>How It Works</li>
  </ul>
  <ul class="footer-col" style="left:920px">
    <li>Solar PV</li><li>Battery Energy Storage</li><li>EV Charging</li><li>Heat Pumps</li>
  </ul>

  <div class="footer-bottom">
    Copyright © 2025 Brightvale Energy. All Rights Reserved.
    <div class="socials"><span></span><span></span><span></span><span></span><span></span></div>
  </div>
  <div class="footer-brand">
    <div class="brand">Brightvale Energy</div>
    <small>Privacy Policy | Terms &amp; Conditions</small>
  </div>
</footer>

</body>
</html>
```